" Um grupo de investidores brasileiros e portugueses foi formado para lançar um condomínio em Portugal, nos arredores de Lisboa. A construtora, Zeva! Módulos, é especializada em casas feitas com containers. Vejam nosso instagram @rimo.brisal para conhecer mais sobre o nosso mercado. Apesar das casas serem container, neste projeto elas serão revestidas externamente, será um condomínio de luxo, porém com estilo mais moderno. "

```html
<!DOCTYPE html>
<html lang="pt-BR">
<head>
<meta charset="UTF-8">
<title>Papel timbrado – Quinta Alvorada</title>
<link href="https://fonts.googleapis.com/css2?family=Quicksand:wght@400;500&display=swap" rel="stylesheet">
<style>
  :root {
    --backdrop: #e9e7e3;
    --paper: #ffffff;
    --brand-green: #7cbf2f;
    --text-grey: #8a8a8a;
    --mark-faint: #eeede8;
  }
  * { margin: 0; padding: 0; box-sizing: border-box; }
  html, body {
    width: 1200px; height: 1200px; overflow: hidden;
    background: var(--backdrop);
    font-family: "Quicksand", sans-serif;
  }
  .letterhead {
    position: absolute; left: 204px; top: 40px;
    width: 792px; height: 1120px;
    background: var(--paper);
    border-right: 10px solid var(--brand-green);
    box-shadow: 0 4px 18px rgba(0,0,0,0.12);
  }
  .brand {
    position: absolute; top: 58px; left: 0; right: 0;
    display: flex; justify-content: center; align-items: center; gap: 14px;
  }
  .brand-dot {
    width: 54px; height: 54px; border-radius: 50%;
    background: var(--brand-green);
  }
  .brand-name {
    font-size: 40px; font-weight: 400; letter-spacing: 3px;
    color: var(--brand-green); text-transform: uppercase;
  }
  .brand-watermark {
    position: absolute; left: 146px; top: 300px;
    width: 500px; height: 500px; border-radius: 50%;
    background: var(--mark-faint);
  }
  .contact-footer {
    position: absolute; bottom: 44px; left: 60px; right: 60px;
    display: flex; justify-content: space-between; align-items: center;
  }
  .contact-item { display: flex; align-items: center; gap: 8px; }
  .contact-icon {
    width: 22px; height: 22px; border-radius: 4px;
    background: var(--brand-green);
    display: flex; align-items: center; justify-content: center;
    flex-shrink: 0;
  }
  .contact-text {
    font-size: 10px; line-height: 1.45; color: var(--text-grey);
  }
</style>
</head>
<body>
  <main class="letterhead">
    <header class="brand">
      <span class="brand-dot"></span>
      <span class="brand-name">Quinta Alvorada</span>
    </header>

    <div class="brand-watermark" aria-hidden="true"></div>

    <footer class="contact-footer">
      <div class="contact-item">
        <span class="contact-icon">
          <svg width="14" height="14" viewBox="0 0 24 24"><path fill="#fff" d="M6.6 10.8a15.1 15.1 0 0 0 6.6 6.6l2.2-2.2a1 1 0 0 1 1-.25 11.4 11.4 0 0 0 3.6.57 1 1 0 0 1 1 1V20a1 1 0 0 1-1 1A17 17 0 0 1 3 4a1 1 0 0 1 1-1h3.5a1 1 0 0 1 1 1c0 1.25.2 2.45.57 3.57a1 1 0 0 1-.25 1z"/></svg>
        </span>
        <p class="contact-text">(21) 98765-4321<br>(21) 91234-5678</p>
      </div>
      <div class="contact-item">
        <span class="contact-icon">
          <svg width="14" height="14" viewBox="0 0 24 24"><path fill="#fff" d="M12 2a7 7 0 0 0-7 7c0 5.2 7 13 7 13s7-7.8 7-13a7 7 0 0 0-7-7zm0 9.5A2.5 2.5 0 1 1 12 6.5a2.5 2.5 0 0 1 0 5z"/></svg>
        </span>
        <p class="contact-text">Av. Rio Azul, Nº 310 – Bairro<br>Centro, Cidade/UF CEP 12345-678</p>
      </div>
      <div class="contact-item">
        <span class="contact-icon">
          <svg width="14" height="14" viewBox="0 0 24 24"><path fill="#fff" d="M3 5h18a1 1 0 0 1 1 1v12a1 1 0 0 1-1 1H3a1 1 0 0 1-1-1V6a1 1 0 0 1 1-1zm9 7.5L4 7.5V9l8 5 8-5V7.5z"/></svg>
        </span>
        <p class="contact-text">contato@quintaalvorada.com.br<br>www.quintaalvorada.com.br</p>
      </div>
    </footer>
  </main>
</body>
</html>
```